Analytics software company needs a business card design

We need a business card design for a global analytics software provider called 'Varnel Software'. Our main focus is developing real estate analysis software. We are open to any color scheme. The final design should be simple, modern, and precise.
Updates

There is one day left in our project and we are still looking forward to receiving additional submissions. We look forward to selecting one of your designs. Thanks.

Industry/Entity Type

Real Estate

```html
<!DOCTYPE html>
<html lang="en">
<head>
<meta charset="utf-8">
<title>Varnel Software – Business Card</title>
<link href="https://fonts.googleapis.com/css2?family=Cinzel:wght@400;500&display=swap" rel="stylesheet">
<style>
  :root {
    --page: #ffffff;
    --ink: #111111;
    --card-edge: #d4d4d4;
    --navy-deep: #122a4f;
    --blue: #1f7fae;
    --blue-light: #a9dcf1;
    --back-top: #1c365c;
    --back-bottom: #0c2244;
    --back-text: #d5e4f3;
  }
  * { margin: 0; padding: 0; box-sizing: border-box; }
  html, body {
    width: 1200px; height: 900px; overflow: hidden;
    background: var(--page);
  }
  .sheet { position: relative; width: 1200px; height: 900px; }

  .side-label {
    position: absolute; left: 95px;
    font-family: "Cinzel", serif; font-size: 42px; font-weight: 400;
    color: var(--ink); letter-spacing: 1px; line-height: 1;
  }
  .side-label--front { top: 238px; }
  .side-label--back { top: 614px; }

  .card { position: absolute; overflow: hidden; }

  .card--front {
    left: 365px; top: 72px; width: 672px; height: 337px;
    background: var(--page);
    border: 1px solid var(--card-edge);
  }
  .front-art {
    position: absolute; left: 250px; top: 0; right: 0; bottom: 0;
    border-bottom-left-radius: 190px 337px;
    background:
      radial-gradient(ellipse 200px 170px at 58% 45%, var(--blue-light), var(--blue) 60%, transparent 100%),
      linear-gradient(100deg, var(--navy-deep) 0%, #1a5c93 40%, var(--blue) 100%);
  }
  .brand-mark {
    position: absolute; left: 78px; top: 106px;
    width: 80px; height: 80px;
    background: var(--navy-deep);
  }
  .company-name {
    position: absolute; left: 33px; top: 256px;
    font-family: "Cinzel", serif; font-size: 27px; font-weight: 500;
    color: var(--ink); letter-spacing: 0.5px; white-space: nowrap;
  }

  .card--back {
    left: 377px; top: 495px; width: 654px; height: 328px;
  }
  .back-art {
    position: absolute; inset: 0;
    background:
      radial-gradient(ellipse 90px 260px at 50% 75%, rgba(150,205,240,0.75), rgba(95,168,220,0.25) 55%, transparent 100%),
      radial-gradient(ellipse 230px 140px at 50% 100%, rgba(95,168,220,0.35), transparent 100%),
      linear-gradient(180deg, var(--back-top), var(--back-bottom));
  }
  .back-copy {
    position: absolute;
    font-family: "Cinzel", serif; font-size: 12.5px; line-height: 15.6px;
    color: var(--back-text); text-align: center; text-transform: uppercase;
    white-space: nowrap;
  }
  .back-copy--left { left: 14px; top: 65px; width: 170px; }
  .back-copy--right { left: 340px; top: 48px; width: 310px; }
</style>
</head>
<body>
<main class="sheet">
  <p class="side-label side-label--front">FRONT</p>
  <p class="side-label side-label--back">BACK</p>

  <section class="card card--front" aria-label="Business card front">
    <div class="front-art" role="img" aria-label="Flowing blue abstract wave artwork"></div>
    <div class="brand-mark" aria-hidden="true"></div>
    <h1 class="company-name">VARNEL SOFTWARE</h1>
  </section>

  <section class="card card--back" aria-label="Business card back">
    <div class="back-art" role="img" aria-label="Glowing blue digital skyline of data columns on a dark navy background"></div>
    <p class="back-copy back-copy--left">Lorem Ipsum is simply<br>dummy text of the<br>printing and<br>typesetting<br>industry. Lorem</p>
    <p class="back-copy back-copy--right">Lorem Ipsum is simply dummy text of the<br>printing and typesetting industry.<br>Lorem Ipsum has been the industry's<br>standard dummy text ever since<br>the 1500s when an unknown<br>printer. took a<br>galley of type<br>and scramb<br>ed itto make<br>type specimen<br>book.</p>
  </section>
</main>
</body>
</html>
```